Personal Motivational Quote Poster Design

I would like to create a poster with some of my favorite quotes to hang in my office. I did similar projects in 2012 and 2014. I've uploaded the winning designs so you can get a better idea of what I'm looking for. I will provide feedback on your design within 24 hours of receiving it.

The poster must contain the following quotes:

“What the pupil must learn, if he learns anything at all, is that the world will do most of the work for you, provided you cooperate with it by identifying how it really works and aligning with those realities. If we do not let the world teach us, it teaches us a lesson.” - Walter Brindley

“I tackle every big new problem by asking two questions: Who has dealt with this problem well? And what can we learn from them?” - Hal Porter

“If we can really understand the problem, the answer will come out of it, because the answer is not separate from the problem.” - Ravel Ondashanti

“Success is nothing more than a few simple disciplines, practiced every day; while failure is simply a few errors in judgment, repeated every day. It is the accumulative weight of our disciplines and our judgments that leads us to either fortune or failure.” - Ned Calve

“Inaction breeds doubt and fear. Action breeds confidence and courage.” - Rex Halloway

“What’s the one thing you can do, such that by doing it, everything else will be easier or unnecessary?” - Lyle Danvers

Requirements
Must have
• The poster will be 24" high x 36" long and printed on canvas, so the image you create needs to have a resolution of at least 2700 x 3900.
Nice to have
• I don't have an exact vision for how the poster should look, so I am totally open to you using your creativity to develop, arrange and present the content as you'd like.

That said, I would like an image (photo or posterized image) of the person being quoted along with each quote. I do not have specific images that I would like you to use, so you will need to find the images on your own.

The images don't need to be perfect... I am more interested in the poster relating the essence of the quotes and the people being quoted than I am in perfect photographic images of the people being quoted.

```html
<!DOCTYPE html>
<html lang="en">
<head>
<meta charset="utf-8">
<title>Quote Poster</title>
<link rel="stylesheet" href="https://fonts.googleapis.com/css2?family=Montserrat:ital,wght@0,400;0,500;1,400&display=swap">
<style>
  :root {
    --page: #2a2a2c;
    --mint: #93e3d2;
    --ink: #1b1b24;
    --pink: #f6c3cc;
    --violet: #877dda;
    --mist: #e2e2e4;
    --sky: #78c9f6;
    --leaf: #a9e79b;
    --butter: #f8f5bb;
    --photo-light: #c9c9c9;
    --photo-dark: #4a4a4a;
    --bar: #f4f4f4;
  }
  * { box-sizing: border-box; margin: 0; padding: 0; }
  html, body { width: 1200px; height: 800px; overflow: hidden; }
  body {
    background: var(--page);
    display: flex;
    align-items: center;
    justify-content: center;
    font-family: "Montserrat", sans-serif;
    color: var(--ink);
  }
  .poster {
    width: 624px;
    height: 760px;
    background: var(--mint);
    padding: 22px 34px;
    display: flex;
    flex-direction: column;
    justify-content: space-between;
  }
  .quote-row {
    position: relative;
    height: 112px;
  }
  .portrait {
    position: absolute;
    top: 0;
    width: 140px;
    height: 112px;
    border: 1.5px solid var(--ink);
    background: var(--bar);
    z-index: 2;
    display: flex;
    flex-direction: column;
  }
  .window-bar {
    height: 9px;
    display: flex;
    justify-content: flex-end;
    align-items: center;
    padding-right: 4px;
    border-bottom: 1.5px solid var(--ink);
  }
  .window-bar svg { display: block; }
  .portrait-fill {
    flex: 1;
    background: linear-gradient(160deg, var(--photo-light), var(--photo-dark));
  }
  .quote-band {
    position: absolute;
    top: 10px;
    height: 100px;
    border: 1.5px solid var(--ink);
    display: flex;
    flex-direction: column;
    justify-content: center;
    padding: 0 14px;
    font-size: 9.4px;
    line-height: 1.3;
    box-shadow: 3px 3px 0 var(--ink);
  }
  .quote-band p { text-align: justify; text-align-last: left; }
  .quote-band cite {
    font-style: italic;
    font-size: 9px;
    margin-top: 2px;
    opacity: 0.85;
  }
  .row-left .portrait { left: 10px; }
  .row-left .quote-band { left: 146px; right: 0; }
  .row-right .portrait { right: 0; }
  .row-right .quote-band { left: 0; right: 136px; text-align: right; }
  .row-right .quote-band p { text-align-last: right; }
  .row-right cite { text-align: right; }
  .row-first .portrait { left: 20px; }
  .row-first .quote-band { left: 156px; right: 6px; }
  .band-pink { background: var(--pink); }
  .band-violet { background: var(--violet); }
  .band-mist { background: var(--mist); }
  .band-sky { background: var(--sky); }
  .band-leaf { background: var(--leaf); }
  .band-butter { background: var(--butter); }
</style>
</head>
<body>
<main class="poster">

  <section class="quote-row row-left row-first">
    <figure class="portrait">
      <div class="window-bar"><svg width="22" height="5" viewBox="0 0 22 5"><path d="M0 2.5h4" stroke="#1b1b24"/><rect x="8.5" y="0.5" width="4" height="4" fill="none" stroke="#1b1b24"/><path d="M17 0.5l4 4M21 0.5l-4 4" stroke="#1b1b24"/></svg></div>
      <div class="portrait-fill" role="img" aria-label="Black and white portrait of Walter Brindley"></div>
    </figure>
    <blockquote class="quote-band band-pink">
      <p>“What the pupil must learn, if he learns anything at all, is that the world will do most of the work for you, provided you cooperate with it by identifying how it really works and aligning with those realities. If we do not let the world teach us, it teaches us a lesson.”</p>
      <cite>Walter Brindley</cite>
    </blockquote>
  </section>

  <section class="quote-row row-right">
    <blockquote class="quote-band band-violet">
      <p>“I tackle every big new problem by asking two questions: Who has dealt with this problem well? And what can we learn from them?”</p>
      <cite>Hal Porter</cite>
    </blockquote>
    <figure class="portrait">
      <div class="window-bar"><svg width="22" height="5" viewBox="0 0 22 5"><path d="M0 2.5h4" stroke="#1b1b24"/><rect x="8.5" y="0.5" width="4" height="4" fill="none" stroke="#1b1b24"/><path d="M17 0.5l4 4M21 0.5l-4 4" stroke="#1b1b24"/></svg></div>
      <div class="portrait-fill" role="img" aria-label="Black and white portrait of Hal Porter"></div>
    </figure>
  </section>

  <section class="quote-row row-left">
    <figure class="portrait">
      <div class="window-bar"><svg width="22" height="5" viewBox="0 0 22 5"><path d="M0 2.5h4" stroke="#1b1b24"/><rect x="8.5" y="0.5" width="4" height="4" fill="none" stroke="#1b1b24"/><path d="M17 0.5l4 4M21 0.5l-4 4" stroke="#1b1b24"/></svg></div>
      <div class="portrait-fill" role="img" aria-label="Black and white portrait of Ravel Ondashanti"></div>
    </figure>
    <blockquote class="quote-band band-mist">
      <p>“If we can really understand the problem, the answer will come out of it, because the answer is not separate from the problem.”</p>
      <cite>Ravel Ondashanti</cite>
    </blockquote>
  </section>

  <section class="quote-row row-right">
    <blockquote class="quote-band band-sky">
      <p>“Success is nothing more than a few simple disciplines, practiced every day; while failure is simply a few errors in judgment, repeated every day. It is the accumulative weight of our disciplines and our judgments that leads us to either fortune or failure.”</p>
      <cite>Ned Calve</cite>
    </blockquote>
    <figure class="portrait">
      <div class="window-bar"><svg width="22" height="5" viewBox="0 0 22 5"><path d="M0 2.5h4" stroke="#1b1b24"/><rect x="8.5" y="0.5" width="4" height="4" fill="none" stroke="#1b1b24"/><path d="M17 0.5l4 4M21 0.5l-4 4" stroke="#1b1b24"/></svg></div>
      <div class="portrait-fill" role="img" aria-label="Black and white portrait of Ned Calve"></div>
    </figure>
  </section>

  <section class="quote-row row-left">
    <figure class="portrait">
      <div class="window-bar"><svg width="22" height="5" viewBox="0 0 22 5"><path d="M0 2.5h4" stroke="#1b1b24"/><rect x="8.5" y="0.5" width="4" height="4" fill="none" stroke="#1b1b24"/><path d="M17 0.5l4 4M21 0.5l-4 4" stroke="#1b1b24"/></svg></div>
      <div class="portrait-fill" role="img" aria-label="Black and white portrait of Rex Halloway"></div>
    </figure>
    <blockquote class="quote-band band-leaf">
      <p>“Inaction breeds doubt and fear. Action breeds confidence and courage.”</p>
      <cite>Rex Halloway</cite>
    </blockquote>
  </section>

  <section class="quote-row row-right">
    <blockquote class="quote-band band-butter">
      <p>“What’s the one thing you can do, such that by doing it, everything else will be easier or unnecessary?”</p>
      <cite>Lyle Danvers</cite>
    </blockquote>
    <figure class="portrait">
      <div class="window-bar"><svg width="22" height="5" viewBox="0 0 22 5"><path d="M0 2.5h4" stroke="#1b1b24"/><rect x="8.5" y="0.5" width="4" height="4" fill="none" stroke="#1b1b24"/><path d="M17 0.5l4 4M21 0.5l-4 4" stroke="#1b1b24"/></svg></div>
      <div class="portrait-fill" role="img" aria-label="Black and white portrait of Lyle Danvers"></div>
    </figure>
  </section>

</main>
</body>
</html>
```